Event Ticketing homepage design

This contest is for an event ticketing homepage to be based on the script - http://www.galvorin-passhub.example/demo5/index.php.

Similar ticketing systems for which ideas can be generated are: tollaquin dotcom, brisemark dotcom and quorvilla dotcom.

The homepage these will be based on this design: http://www.plimvey.example/nl/home.html

Features that the design should have include:

1. All positions shown in the demo
2. Top navigation menu: Left hand side - Social A and Social B icons, Add event. Right hand side – Sign Up, Sign In, Forgot Password
3. Featured events with “buy now” buttons
4. Search function
5. Social A connect (near login)
6. Create event (see tollaquin dotcom)
7. Most viewed (see brisemark dotcom)
8. Best sellers (see brisemark dotcom)
9. Main Menu navigation buttons: Home,
10. About us, How to advertise, Policies, How to purchase, Terms and Conditions, FAQs, Privacy Policy, Contact Us, Copyright in the footer
11. Hot spots (see quorvilla dotcom)

I will provide the background image to top designers before choosing a finalist
Final design should have high quality PSD files.
Updates

Reason: Due to request from Lou, i have decided to add 4 more days

Here is the new inspiration http://vardolenworks.example/devpro/DuskHarbor/index.html

Thanks for the designs. We'll be giving feedback to all by the end of today (US eastern time)

Thanks for all designs submitted. As the contest is only one or several designs can be considered and so if I don't leave feedback know that it was not shortlisted to be among the finalists.

Reason: For changes

Industry/Entity Type

Events

```html
<!DOCTYPE html>
<html lang="en">
<head>
<meta charset="utf-8">
<title>Tessaly – Event Ticket Booking</title>
<link href="https://fonts.googleapis.com/css2?family=Open+Sans:wght@400;600;700&family=Russo+One&display=swap" rel="stylesheet">
<style>
:root{
  --navy:#06224a;
  --navy-2:#0b3a78;
  --blue:#1a7fd4;
  --blue-light:#3fb0f0;
  --red:#d01f24;
  --ink:#222;
  --muted:#666;
  --line:#d5dbe3;
  --panel:#f2f5f9;
  --white:#fff;
}
*{box-sizing:border-box;margin:0;padding:0}
html,body{width:769px;height:1200px;overflow:hidden}
body{font-family:"Open Sans",Arial,sans-serif;font-size:9px;color:var(--ink);
  background:linear-gradient(180deg,#0a3a7a 0,#0d4f9a 400px,#0a3a7a 900px,#062a5a 1200px)}
.page{position:relative;width:745px;margin:0 auto;height:1200px}

/* header */
.masthead{height:95px;padding:14px 6px 0;display:flex;justify-content:space-between;color:var(--white)}
.brand-name{font-weight:700;font-size:24px;letter-spacing:1px;color:var(--white)}
.brand-tag{font-size:9px;color:#bcd6f2;margin-top:1px}
.tools{width:300px;font-size:8px}
.tools-row{display:flex;gap:6px;align-items:center}
.tools-row label{color:#cfe2f7}
.field{background:var(--white);height:14px;border:1px solid #8fb6e0;color:#999;padding:1px 4px;font-size:8px}
.loc{width:110px}.search{width:120px}
.social{display:flex;gap:4px;margin-left:auto}
.social span{width:14px;height:14px;background:#2c6cc0;border:1px solid #7fb2ea}
.date{margin-top:6px;text-align:right;color:#cfe2f7}

/* nav */
.main-nav{position:absolute;top:62px;left:0;right:0;height:20px;display:flex;
  background:linear-gradient(#3aa8ee,#1a72c4);border-top:1px solid #7cc6f5}
.main-nav a{color:var(--white);text-decoration:none;font-size:9px;padding:0 12px;line-height:20px;border-right:1px solid #5cb4ea}
.main-nav a.on{background:var(--white);color:var(--navy-2);font-weight:700}
.sub-nav{position:absolute;top:82px;left:0;right:0;height:16px;background:var(--white);display:flex;align-items:center;padding-left:8px}
.sub-nav a{color:var(--navy-2);font-size:8px;text-decoration:none;padding:0 10px;border-right:1px solid var(--line)}

/* hero */
.hero{position:absolute;top:108px;left:0;right:0;height:290px;display:flex;background:var(--white);padding:4px}
.hero-main{flex:1;position:relative;background:linear-gradient(160deg,#3a2a2a 0,#a8552a 35%,#d9a060 55%,#4b4a6a 100%);overflow:hidden}
.hero-side{width:170px;margin-left:4px;position:relative;background:linear-gradient(170deg,#7a2a12,#d26a1e 50%,#5a1e30)}
.hero-title{position:absolute;top:12px;left:14px;font-family:"Russo One",sans-serif;font-size:30px;color:var(--white);letter-spacing:1px}
.hero-copy{position:absolute;left:14px;bottom:42px;width:330px;color:var(--white);font-weight:700;font-size:11px;line-height:14px}
.read-more{position:absolute;left:280px;bottom:18px;background:var(--blue);color:var(--white);font-weight:700;font-size:9px;padding:4px 10px;border-radius:2px}
.dots{position:absolute;bottom:6px;left:210px;display:flex;gap:4px}
.dots i{width:7px;height:7px;border-radius:50%;background:#fff;opacity:.5}.dots i:first-child{opacity:1}
.side-copy{position:absolute;left:8px;bottom:24px;right:8px;color:var(--white);font-size:8px;font-weight:700;line-height:11px}

/* carousel */
.carousel{position:absolute;top:404px;left:0;right:0;height:86px;background:var(--white);display:flex;align-items:center;padding:0 6px;gap:6px;border-bottom:1px solid var(--line)}
.arrow{width:14px;height:30px;background:var(--panel);display:flex;align-items:center;justify-content:center}
.shows{flex:1;display:flex;gap:7px}
.show{flex:1;text-align:center;font-size:7px;color:var(--muted)}
.show .pic{height:54px;margin-bottom:3px}

/* middle */
.middle{position:absolute;top:496px;left:0;right:0;height:345px;background:var(--white);display:flex;gap:8px;padding:6px}
.box-head{background:linear-gradient(#3fb0f0,#1a7fd4);color:var(--white);font-weight:700;font-size:9px;padding:3px 6px}
.popular{width:120px}
.popular ul{list-style:none;border:1px solid var(--line);border-top:0;padding:4px 6px}
.popular li{font-size:8px;line-height:12.4px;color:var(--ink)}
.popular li::before{content:"› ";color:var(--blue)}
.promo{margin-top:6px;height:90px;background:linear-gradient(135deg,#f2c21a,#e56a12 60%,#2a6cc0)}
.featured{flex:1}
.event{display:flex;align-items:center;height:51px;border-bottom:1px solid var(--line);padding:0 4px;gap:8px}
.event .logo{width:80px;height:36px}
.event .what{width:130px;font-size:8px;line-height:11px}
.event .where{flex:1;font-size:8px;line-height:11px}
.event .where b{color:var(--blue)}
.buy{background:var(--red);color:var(--white);font-weight:700;font-size:8px;padding:3px 7px;border-radius:2px}
.account{width:120px;display:flex;flex-direction:column;gap:6px}
.form{border:1px solid var(--line);background:var(--panel);padding:5px 6px}
.form label{display:block;font-size:7.5px;color:var(--muted);margin-top:3px}
.form .field{display:block;width:100%;height:12px;border-color:var(--line)}
.btn{display:inline-block;margin-top:5px;background:var(--blue);color:var(--white);font-size:8px;padding:2px 8px;border-radius:2px}
.check{font-size:7.5px;color:var(--muted);margin-top:4px}
.hotspot{height:58px;background:linear-gradient(160deg,#1a1a3a,#4a2a7a 50%,#c84a9a)}

/* lists */
.lists{position:absolute;top:848px;left:0;right:0;height:236px;background:var(--white);display:flex;gap:8px;padding:6px}
.list{flex:1;border:1px solid var(--line)}
.list .box-head{text-align:center;font-family:"Russo One",sans-serif;font-weight:400;font-size:10px;padding:5px}
.item{display:flex;gap:8px;padding:10px 8px;border-bottom:1px solid var(--line)}
.item .pic{width:62px;height:70px;flex:none}
.item p{font-size:7.5px;line-height:10px;color:var(--ink)}
.item .buy{display:inline-block;margin-top:8px}
.item .link{color:var(--red);font-weight:700;font-size:8px;margin-top:8px}

/* footer */
.site-footer{position:absolute;top:1104px;left:0;right:0;text-align:center;color:#cfe2f7;font-size:8px}
.site-footer nav a{color:#cfe2f7;text-decoration:none;padding:0 6px;border-right:1px solid #4c78b0}
.site-footer nav a:last-child{border:0}
.site-footer p{margin-top:14px}
</style>
</head>
<body>
<div class="page">
  <header class="masthead">
    <div>
      <div class="brand-name">TESSALY</div>
      <div class="brand-tag">Event Ticket Booking Company</div>
    </div>
    <div class="tools">
      <div class="tools-row">
        <label>Location</label><label style="margin-left:80px">Search</label>
        <div class="social"><span aria-label="Social A"></span><span aria-label="Social B"></span><span aria-label="Share"></span></div>
      </div>
      <div class="tools-row" style="margin-top:2px">
        <div class="field loc">Enter your city</div>
        <div class="field search">Search events</div>
      </div>
      <div class="date">Sun Sep 15, 2013 | 12:10 PM</div>
    </div>
  </header>

  <nav class="main-nav">
    <a class="on" href="#">Home</a><a href="#">How to advertise</a><a href="#">Policies</a><a href="#">How to purchase</a><a href="#">FAQs</a><a href="#">Contact Us</a>
  </nav>
  <nav class="sub-nav"><a href="#">Local Events</a><a href="#">Top Movies</a><a href="#">Top Events</a></nav>

  <section class="hero">
    <div class="hero-main" role="img" aria-label="Concert stage with crowd and lights">
      <div class="hero-title">POPULAR EVENTS</div>
      <p class="hero-copy">Lorem ipsum dolor sit amet, consectetur adipiscing elit, sed do eiusmod tempor incididunt ut labore et dolore magna aliqua. Ut enim ad minim veniam.</p>
      <span class="read-more">READ MORE</span>
      <div class="dots"><i></i><i></i><i></i><i></i></div>
    </div>
    <div class="hero-side" role="img" aria-label="Festival fireworks scene">
      <p class="side-copy">Lorem ipsum dolor sit amet, consectetur adipiscing elit sed do.</p>
    </div>
  </section>

  <section class="carousel">
    <div class="arrow"><svg width="8" height="10"><path d="M6 1 2 5l4 4" stroke="#1a7fd4" stroke-width="2" fill="none"/></svg></div>
    <div class="shows">
      <div class="show"><div class="pic" role="img" aria-label="Show poster" style="background:linear-gradient(#ddd,#555)"></div>Echo the Musical</div>
      <div class="show"><div class="pic" role="img" aria-label="Show poster" style="background:linear-gradient(#c9a06a,#5a3a1a)"></div>Riding Miss Clover</div>
      <div class="show"><div class="pic" role="img" aria-label="Show poster" style="background:linear-gradient(#e23a2a,#7a1a3a)"></div>Festive Panto</div>
      <div class="show"><div class="pic" role="img" aria-label="Show poster" style="background:linear-gradient(#222,#6a6a6a)"></div>Harbor Boys</div>
      <div class="show"><div class="pic" role="img" aria-label="Show poster" style="background:linear-gradient(#3a5a9a,#111)"></div>Garden Stage</div>
      <div class="show"><div class="pic" role="img" aria-label="Show poster" style="background:linear-gradient(#8a6a4a,#2a1a1a)"></div>Quiet Lanes</div>
      <div class="show"><div class="pic" role="img" aria-label="Show poster" style="background:linear-gradient(#444,#aaa)"></div>The Brass</div>
    </div>
    <div class="arrow"><svg width="8" height="10"><path d="M2 1l4 4-4 4" stroke="#1a7fd4" stroke-width="2" fill="none"/></svg></div>
  </section>

  <section class="middle">
    <aside class="popular">
      <div class="box-head">POPULAR EVENTS</div>
      <ul>
        <li>Red Ember Peppers</li><li>Frostline Festival</li><li>North Harbor Blues</li><li>The Drumline</li><li>Ship Show</li><li>Bard Nights</li><li>Silent The Musical</li><li>Comedy Tour London</li><li>Gearhouse Live</li><li>Riverside Live</li><li>Meadow Pride 2013</li><li>Boxer Mary</li><li>Huxton</li><li>Choral Arts Night</li><li>The Weald 2013</li>
      </ul>
      <div class="promo" role="img" aria-label="Help desk 24/7 sponsor advert"></div>
    </aside>

    <div class="featured">
      <div class="box-head">FEATURED EVENTS</div>
      <div class="event"><div class="logo" role="img" aria-label="Event flyer" style="background:linear-gradient(#1a4a8a,#0a2a5a)"></div><div class="what">Driftday Sunday presents Marlow Vance and Idris Fell</div><div class="where"><b>TIDEWATER DECK CLUB</b><br>Las Vegas, NV</div><span class="buy">BUY NOW</span></div>
      <div class="event"><div class="logo" role="img" aria-label="Halvern venue badge" style="background:#111"></div><div class="what">Driftday Sunday presents Marlow Vance and Idris Fell</div><div class="where"><b>TIDEWATER DECK CLUB</b><br>Las Vegas, NV</div><span class="buy">BUY NOW</span></div>
      <div class="event"><div class="logo" role="img" aria-label="Event flyer" style="background:linear-gradient(#e8e8e8,#9a9a9a)"></div><div class="what">Driftday Sunday presents Marlow Vance and Idris Fell</div><div class="where"><b>TIDEWATER DECK CLUB</b><br>Las Vegas, NV</div><span class="buy">BUY NOW</span></div>
      <div class="event"><div class="logo" role="img" aria-label="Orvane artist badge" style="background:#222"></div><div class="what">Driftday Sunday presents Marlow Vance and Idris Fell</div><div class="where"><b>TIDEWATER DECK CLUB</b><br>Las Vegas, NV</div><span class="buy">BUY NOW</span></div>
      <div class="event"><div class="logo" role="img" aria-label="Lumen Collective badge" style="background:#dcdcdc"></div><div class="what">Driftday Sunday presents Marlow Vance and Idris Fell</div><div class="where"><b>TIDEWATER DECK CLUB</b><br>Las Vegas, NV</div><span class="buy">BUY NOW</span></div>
    </div>

    <aside class="account">
      <div>
        <div class="box-head">Sign in</div>
        <div class="form">
          <label>User Name</label><span class="field"></span>
          <label>Password</label><span class="field"></span>
          <span class="btn">Sign in</span>
        </div>
      </div>
      <div>
        <div class="box-head">Sign Up</div>
        <div class="form">
          <label>User Name</label><span class="field"></span>
          <label>Password</label><span class="field"></span>
          <label>Email</label><span class="field"></span>
          <div class="check">&#9744; Forgot Password</div>
          <span class="btn">Sign up</span>
        </div>
      </div>
      <div>
        <div class="box-head">Hot Spot</div>
        <div class="hotspot" role="img" aria-label="Nightclub hot spot photo"></div>
      </div>
    </aside>
  </section>

  <section class="lists">
    <div class="list">
      <div class="box-head">BEST SELLERS</div>
      <div class="item"><div class="pic" role="img" aria-label="Event poster" style="background:linear-gradient(#333,#888)"></div><div><p>12/10/2013<br>ORVANE FRESH WEEK 2013<br>BRACKWELL MUSIC HALL<br>LONDON, UK</p><span class="buy">BUY NOW</span></div></div>
      <div class="item"><div class="pic" role="img" aria-label="Event poster" style="background:linear-gradient(#444,#999)"></div><div><p>12/10/2013<br>ORVANE FRESH WEEK 2013<br>BRACKWELL MUSIC HALL<br>LONDON, UK</p><span class="buy">BUY NOW</span></div></div>
    </div>
    <div class="list">
      <div class="box-head">MOST VIEWED</div>
      <div class="item"><div class="pic" role="img" aria-label="Concert photo" style="background:linear-gradient(#2a2a2a,#8a6a3a)"></div><div><p>12/10/2013<br>ORVANE FRESH WEEK 2013<br>BRACKWELL MUSIC HALL<br>LONDON, UK</p><span class="buy">BUY NOW</span></div></div>
      <div class="item"><div class="pic" role="img" aria-label="Concert photo" style="background:linear-gradient(#1a2a4a,#6a7a9a)"></div><div><p>12/10/2013<br>ORVANE FRESH WEEK 2013<br>BRACKWELL MUSIC HALL<br>LONDON, UK</p><span class="buy">BUY NOW</span></div></div>
    </div>
    <div class="list">
      <div class="box-head">FEATURED VENUES</div>
      <div class="item"><div class="pic" role="img" aria-label="Venue photo" style="background:linear-gradient(#1a1a1a,#6a3a2a)"></div><div><p>THE TUNE ROOM<br>Los Angeles, CA</p><div class="link">GET IN</div></div></div>
      <div class="item"><div class="pic" role="img" aria-label="Venue photo" style="background:linear-gradient(#2a1a3a,#7a4a9a)"></div><div><p>AVENOR HOLLYWOOD<br>Los Angeles, CA</p><div class="link">GET IN</div></div></div>
    </div>
  </section>

  <footer class="site-footer">
    <nav><a href="#">About us</a><a href="#">How to advertise</a><a href="#">Policies</a><a href="#">How to purchase</a><a href="#">Terms and Conditions</a><a href="#">FAQs</a><a href="#">Privacy Policy</a><a href="#">Contact Us</a></nav>
    <p>Copyright &copy; TESSALY. All Rights Reserved</p>
  </footer>
</div>
</body>
</html>
```